Webdesign für einen Softwarehersteller
Zielgruppe
Wir sind Softwarehersteller einer Arbeitsschutz Management Software. Unser Leistungsumfang beträgt
a) die Analyse, Beurteilung und Risikoeinschätzung von Gefährdungen an einem Arbeitsplatz, einer Maschine oder Tätigkeit
b) die Unterweisung von Mitarbeitern
c) ein Risiko- und Maßnahmenmanagement
d) ein Unfallmanagement bei welchem Unfälle erfasst, ausgewertet und präventive Maßnahmen ergriffen werden
e) ein Management zur Verwaltung von Gefahrstoffen inkl. der Ableitung von präventiven Maßnahmen
f) ein Tool zur Auditierung von Prozessen, wie z.B. ISO-Normen
Unsere Zielgruppe sind Industrieunternehmen ab 500 Mitarbeitern. Der Traumkunde hat 4000 - 8000 Mitarbeiter. Unsere Software ist multilingual und kann auch weltweit eingesetzt werden womit auch weltweit operierende Konzerne zu unserer Zielgruppe gehören.
Mit unserer Software dokumentiert das Unternehmen alle notwendigen Prozesse zur Einhaltung des Arbeitsschutzes. Die Software unterstützt dabei das Unternehmen, die Menschen im Unternehmen best möglich zu schützen und allen rechtlichen Anforderungen gerecht zu werden.
Aufgabenstellung
Hallo Designer:innen,
zuerst möchte ich mich bei euch bedanken, dass Ihr euch an unserem Projekt beteiligt. Wir suchen eine Homepage, sehr clean, sehr modern und passend zu einem Softwareprodukt z.B. https://brennlaub.com/seiten-vorlagen (Kalvorix Theme). Wir legen Wert auf Struktur, Übersichtlichkeit, Modern.
Textinhalte findet Ihr auf der bestehenden Homepage.
WICHTIG!!!
a) Die bestehende Homepage dient als Inhaltsvorlage. Wir finden die Homepage nicht gut!
b) Wir erwarten, ein Hochwertiges Design sowie eine durchdachte Aufteilung der Homepage. Wenn Ihr z.B. der Meinung seid, dass auf der Landingpage eine Produktgallerie mit Bildern notwendig ist, dann fügt diese bitte ein und verwendet Demo-Bilder. Wir liefern gerne später Inhalte für die Bereiche. Die neue Webseite darf gerne von der bestehenden Struktur abweichen.
c) Selvadon wird ein neues, moderneres Logo erhalten. Das neue Logo findet Ihr unter
https://stage.selvadon.de/wp-content/uploads/2022/02/test_logo1.png
https://stage478.selvadon.de/wp-content/uploads/2022/03/Logo_web.png

```html
<!DOCTYPE html>
<html lang="de">
<head>
<meta charset="utf-8">
<title>Selvadon – Software für Arbeitsschutz</title>
<link href="https://fonts.googleapis.com/css2?family=Lato:wght@300;400;700;900&display=swap" rel="stylesheet">
<style>
:root{
  --green-dark:#4b6b3d;
  --green:#6db33f;
  --green-line:#7cbf4f;
  --green-pale:#cfe5bf;
  --grey-band:#eeeeea;
  --card:#e6e7e0;
  --text:#3a3a3a;
  --muted:#5d5d5d;
  --white:#ffffff;
}
*{margin:0;padding:0;box-sizing:border-box}
html,body{width:1200px;height:3917px;overflow:hidden;background:var(--white)}
body{font-family:'Lato',sans-serif;color:var(--text);position:relative}
.page{position:absolute;left:108px;top:114px;width:981px;height:3722px;background:var(--white);box-shadow:0 0 14px rgba(0,0,0,.18);overflow:hidden}
.abs{position:absolute}
.btn{position:absolute;display:flex;align-items:center;justify-content:center;border-radius:20px;font-size:11px;font-weight:700;letter-spacing:.5px;text-transform:uppercase;background:var(--green);color:var(--white)}
.btn--ghost{background:transparent;border:1.5px solid var(--white)}
.section-title{position:absolute;left:0;width:100%;text-align:center;font-size:21px;font-weight:400;color:var(--green-dark)}
.section-title::after{content:"";display:block;width:40px;height:2px;background:var(--green-line);margin:9px auto 0}
.photo{position:absolute}
/* hero */
.hero-panel{left:0;top:0;width:396px;height:565px;background:var(--green-dark)}
.hero-photo{left:396px;top:0;width:585px;height:565px;background:linear-gradient(135deg,#e9ebea 0%,#cfd3d2 45%,#9fa4a3 80%,#7d8282 100%)}
.brand{position:absolute;display:flex;align-items:center;gap:6px;font-weight:700;letter-spacing:2px;color:var(--white);font-size:10px}
.brand i{display:block;width:10px;height:10px;background:var(--white)}
.nav{left:103px;top:28px;display:flex;gap:14px;font-size:10px;color:var(--white)}
.nav span.active{border-bottom:1px solid var(--white);padding-bottom:2px}
.hero-title{left:53px;top:163px;font-size:42px;line-height:48px;font-weight:700;color:var(--white)}
.hero-sub{left:53px;top:288px;padding-left:16px;border-left:2px solid var(--green-line);font-size:19px;line-height:25px;font-weight:300;color:var(--white)}
/* card */
.card{left:118px;top:740px;width:756px;height:480px;background:var(--card);border-radius:10px;overflow:hidden}
.card-photo{left:0;top:0;width:431px;height:480px;background:linear-gradient(160deg,#dfe5e6 0%,#b9c2c3 40%,#6f7a7b 75%,#c8cccb 100%)}
.card-label{left:474px;top:52px;font-size:12px;color:var(--green);letter-spacing:.5px}
.card-title{left:474px;top:72px;width:250px;font-size:21px;line-height:23px;color:var(--text)}
.card-text{left:474px;width:245px;font-size:11px;line-height:16.5px;color:var(--muted)}
/* vorteile */
.adv{top:1367px;width:180px}
.adv h4{font-size:13px;font-weight:700;margin-bottom:10px}
.adv p{font-size:9.5px;line-height:16px;color:var(--muted)}
.adv-div{top:1375px;width:1px;height:50px;background:var(--green-line)}
/* band */
.band{left:0;top:1472px;width:981px;height:203px;background:linear-gradient(90deg,#5c7a4d 0%,#6e8a5f 45%,#7f977a 100%)}
.band-title{left:85px;top:1510px;font-size:37px;line-height:40px;font-weight:700;color:var(--white)}
/* features */
.screen{left:52px;top:1861px;width:466px;height:350px;background:linear-gradient(180deg,#f4f5f3 0%,#e2e4e0 100%);border-radius:4px}
.feature{left:586px;width:330px;padding-left:27px}
.feature svg{position:absolute;left:0;top:-3px}
.feature h4{font-size:11px;font-weight:700;margin-bottom:4px}
.feature p{font-size:11px;line-height:16.5px;color:var(--muted)}
/* functions */
.fn-title{left:80px;top:2325px;font-size:22px;color:var(--green-dark)}
.fn-title::after{content:"";display:block;width:40px;height:2px;background:var(--green-line);margin-top:12px}
.fn-text{left:80px;top:2384px;width:320px;font-size:11px;line-height:16.5px;color:var(--muted)}
.grey-band{left:0;top:2450px;width:981px;height:280px;background:var(--grey-band)}
.fn-list{list-style:none;font-size:11px;line-height:20.5px;color:var(--muted)}
.fn-list li::before{content:"+";color:var(--green);font-weight:700;margin-right:9px}
.monitor{left:538px;top:2317px;width:327px;height:380px;background:linear-gradient(180deg,#3c3f3c 0%,#d9dcd6 55%,#c6c8c5 100%);border-radius:6px}
/* clients */
.client{top:2890px;width:170px;text-align:center;font-size:26px;font-weight:900;color:#2b2b2b;letter-spacing:1px}
/* person */
.person-band{left:0;top:2993px;width:981px;height:433px;background:var(--grey-band)}
.portrait{left:55px;top:2928px;width:204px;height:205px;background:linear-gradient(180deg,#d8dde0 0%,#eef0f1 100%)}
.person-name{left:30px;width:255px;top:3245px;text-align:center;font-size:18px;color:var(--green-dark)}
.person-role{left:30px;width:255px;top:3270px;text-align:center;font-size:13px;color:var(--muted)}
.person-text{left:55px;width:205px;top:3310px;text-align:center;font-size:10.5px;line-height:16px;color:var(--muted)}
.about-title{left:331px;top:3112px;font-size:22px;color:var(--green-dark)}
.about-text{left:331px;width:560px;font-size:10.5px;line-height:16px;color:var(--muted)}
/* footer */
.footer{left:0;top:3426px;width:981px;height:240px;background:var(--green-pale)}
.footer-brand{left:70px;top:3485px;flex-direction:column;gap:8px;font-size:15px;letter-spacing:4px;color:var(--green-dark)}
.footer-brand i{width:26px;height:26px;background:var(--green-dark)}
.footer-text{left:72px;top:3574px;width:190px;font-size:10.5px;line-height:15px;color:var(--green-dark)}
.fcol h5{font-size:9.5px;font-weight:400;letter-spacing:.5px;color:var(--green-dark);margin-bottom:12px}
.fcol ul{list-style:none;font-size:10.5px;line-height:16.5px;color:var(--green-dark)}
.bottom-bar{left:0;top:3666px;width:981px;height:56px;background:var(--green-dark);color:var(--white);font-size:9.5px}
</style>
</head>
<body>
<div class="page">

  <!-- Hero -->
  <div class="abs hero-panel"></div>
  <div class="photo hero-photo" role="img" aria-label="Foto: Hände an einem Laptop mit geöffneter Arbeitsschutz-Software"></div>
  <div class="brand" style="left:28px;top:26px"><i></i>SELVADON</div>
  <nav class="abs nav"><span class="active">Home</span><span>Software module</span><span>Unternehmen</span><span>Kontakt</span></nav>
  <h1 class="abs hero-title">Software für<br>Arbeitsschutz</h1>
  <p class="abs hero-sub">mit einer breiten Palette<br>an Modulen und Funktionen</p>
  <a class="btn" style="left:53px;top:425px;width:108px;height:36px">Entdecken</a>
  <a class="btn btn--ghost" style="left:183px;top:425px;width:155px;height:36px">Warum Selvadon</a>

  <!-- Intro -->
  <h2 class="section-title" style="top:650px">Die Selvadon Arbeitsschutz Software</h2>
  <div class="abs card">
    <div class="photo card-photo" role="img" aria-label="Foto: Person arbeitet am Laptop mit der Software"></div>
    <div class="abs card-label">VORTEILE IHRES GESCHÄFTS</div>
    <h3 class="abs card-title" style="font-weight:400">Lorem ipsum dolor sit amet, consectetur adipiscing elit Selvadon.</h3>
    <p class="abs card-text" style="top:170px">Tellus aliquam accumsan, donec mauris orci orci eget. Viverra magna sollicitudin magna risus vitae, tortor volutpat tristique. Orci vel, at tortor rhoncus, nunc habitant in. Malesuada fermentum ultrices fusce ac dictum ornare euismod.</p>
    <p class="abs card-text" style="top:280px">Tellus aliquam accumsan, donec mauris orci orci eget. Viverra magna sollicitudin magna risus vitae, tortor volutpat tristique. Orci vel, at tortor rhoncus, nunc habitant in. Malesuada fermentum ultrices fusce ac dictum ornare euismod.</p>
    <a class="btn" style="left:474px;top:409px;width:100px;height:27px">Mehr Info</a>
  </div>

  <!-- Vorteile -->
  <h2 class="section-title" style="top:1286px">Lorem Vorteile ipsum</h2>
  <div class="abs adv" style="left:200px"><h4>Vorteil 1</h4><p>Tellus aliquam accan, donec mauris orci orci eget. Viverrasollicitudin</p></div>
  <div class="abs adv-div" style="left:389px"></div>
  <div class="abs adv" style="left:418px"><h4>Vorteil 2</h4><p>Malesuada fermentum ultrices fusce ac dictum ornare euismod.</p></div>
  <div class="abs adv-div" style="left:615px"></div>
  <div class="abs adv" style="left:644px"><h4>Vorteil 3</h4><p>Tellus aliquam accan, donec mauris orci orci eget. Viverrasollicitudin</p></div>

  <!-- Band -->
  <div class="photo band" role="img" aria-label="Foto: lächelnde Mitarbeiter im Büro, grün eingefärbt"></div>
  <h2 class="abs band-title">Lorem Selvadon<br>dolor sit amet&nbsp; ipsum</h2>
  <a class="btn" style="left:85px;top:1614px;width:190px;height:33px">Termin vereinbaren</a>

  <!-- Features -->
  <h2 class="section-title" style="top:1754px">Malesuada fermentum ultrices</h2>
  <div class="photo screen" role="img" aria-label="Bildschirmansicht der Software mit Modulleiste und Auswahllisten"></div>
  <div class="abs feature" style="top:1869px">
    <svg width="18" height="18" viewBox="0 0 18 18"><circle cx="9" cy="9" r="9" fill="var(--green)"/><path d="M9 5v8M5 9h8" stroke="#fff" stroke-width="1.6"/></svg>
    <h4>Vielseitige Entlastung</h4>
    <p>Die Selvadon Arbeitsschutz Software entlastet alle Beteiligten im Arbeitsschutz. Angefangen bei den Vorgesetzten und Fachkräften für Arbeitssicherheit, über die Mitarbeiter mit Schutzfunktionen bis hin zu den IT Administratoren.</p>
  </div>
  <div class="abs feature" style="top:1972px">
    <svg width="18" height="18" viewBox="0 0 18 18"><circle cx="9" cy="9" r="9" fill="var(--green)"/><path d="M9 5v8M5 9h8" stroke="#fff" stroke-width="1.6"/></svg>
    <h4>Hohe Effizienz &amp; Shutz</h4>
    <p>Selvadon besitzt eine Vielzahl an automatisierten Abläufen und Schutzfunktionen. Dadurch werden Mitarbeiter wie auch Verantwortliche optimal geschützt.</p>
  </div>
  <div class="abs feature" style="top:2063px">
    <svg width="18" height="18" viewBox="0 0 18 18"><circle cx="9" cy="9" r="9" fill="var(--green)"/><path d="M9 5v8M5 9h8" stroke="#fff" stroke-width="1.6"/></svg>
    <h4>Perfekte Oberflächen</h4>
    <p>Selvadon bietet eine intuitive, selbsterklärende und sehr einfach zu bedienenden Oberfläche. Dies führt zu einer sehr hohen Akzeptanz und minimalem Schulungsaufwand.</p>
  </div>
  <div class="abs feature" style="top:2154px">
    <svg width="18" height="18" viewBox="0 0 18 18"><circle cx="9" cy="9" r="9" fill="var(--green)"/><path d="M9 5v8M5 9h8" stroke="#fff" stroke-width="1.6"/></svg>
    <h4>Transparente Prozesse</h4>
    <p>Durch das Zusammenwirken aller Module werden Unstimmigkeiten im Arbeitsschutz automatisiert erkannt und per Dashboard dem jeweiligen Verantwortlichen gemeldet.</p>
  </div>

  <!-- Funktionen -->
  <div class="abs grey-band"></div>
  <h2 class="abs fn-title" style="font-weight:400">Funktionen &amp; Module</h2>
  <p class="abs fn-text">Unsere Software für Arbeitsschutz bietet eine breite Palette an Modulen und Funktionen, um Sie im Bereich Arbeitsschutz und Management bestmöglich zu unterstützen:</p>
  <ul class="abs fn-list" style="left:77px;top:2484px">
    <li>Basisfunktionen</li><li>Gefährdungsbeurteilung</li><li>Unterweisung</li><li>Unfallmanagement</li><li>Gefahrstoffmanagement</li><li>Vorsorgeuntersuchungen</li><li>Qualifikationsmatrix</li>
  </ul>
  <ul class="abs fn-list" style="left:272px;top:2484px">
    <li>Maßnahmenmanagement</li><li>Auditierung</li><li>Compliance</li><li>Dateiarchiv</li><li>Controlling und Management</li><li>Multilingual verfügbar</li>
  </ul>
  <a class="btn" style="left:77px;top:2650px;width:190px;height:30px">Funktionen im Detail</a>
  <div class="photo monitor" role="img" aria-label="Monitor mit Ansicht des Gefahrstoffmoduls"></div>

  <!-- Kunden -->
  <h2 class="section-title" style="top:2799px">Selvadon Kundenauszug</h2>
  <div class="abs client" style="left:115px">VARNHOLT</div>
  <div class="abs client" style="left:302px">OSTREL</div>
  <div class="abs client" style="left:475px">KELDEN</div>
  <div class="abs client" style="left:691px">FANDOR</div>

  <!-- Ansprechpartner -->
  <div class="abs person-band"></div>
  <div class="photo portrait" role="img" aria-label="Porträtfoto des Ansprechpartners"></div>
  <div class="abs person-name">Jonas Brendel</div>
  <div class="abs person-role">Ihr persönlicher Ansprechpartner</div>
  <p class="abs person-text">Nehmen Sie jetzt Kontakt auf und vereinbaren Sie Ihren unverbindlichen Beratungs- und Präsentationstermin.</p>
  <h2 class="abs about-title" style="font-weight:400">Wofür steht Selvadon?</h2>
  <p class="abs about-text" style="top:3150px">Als „Selvadon“ wurde in einem römischen Legionslager das Zelt des Befehlshabers bezeichnet – der sicherste Platz im Lager. Prätorianer gehörten der kaiserlichen Gardetruppe an, die das Selvadon beschützt haben. Arbeitsschützer sind die heutigen Prätorianer die das Unternehmen vor Gefahren und Unfällen beschützen!</p>
  <p class="abs about-text" style="top:3218px">Selvadon wird gemeinsam mit unserem Kompetenzteam entwickelt. Zum Kompetenzteam gehören viele Fachkräfte für Arbeitssicherheit die in den Unternehmen direkt an der Basis arbeiten – bis hin zu hochqualifizierten Beratern und Autoren. Diese Mischung macht unsere Software so perfekt, da Sie exakt die Wünsche, Bedürfnisse und Funktionen abbildet, die jeden Tag in den Unternehmen benötigt werden.</p>
  <a class="btn" style="left:331px;top:3320px;width:257px;height:36px">Präsentationstermin vereinbaren</a>

  <!-- Footer -->
  <footer>
    <div class="abs footer"></div>
    <div class="brand footer-brand"><i></i>SELVADON</div>
    <p class="abs footer-text">Lorem ipsum dolor sit amet, dolor consectetur adipiscing elit. Sit amet, consectetur adipiscing elit.</p>
    <div class="abs fcol" style="left:351px;top:3486px"><h5>ARBEITSSCHUTZ SOFTWARE MODULE</h5><ul><li>Basisfunktionen</li><li>Gefährdungsbeurteilung</li><li>Unterweisung</li><li>Unfallmanagement</li><li>Gefahrstoffmanagement</li><li>Auditierung</li><li>Compliance</li></ul></div>
    <div class="abs fcol" style="left:606px;top:3486px"><h5>INFORMATIONEN</h5><ul><li>Unternehmen</li><li>Präsentationstermin</li><li>Kontakt</li></ul></div>
    <div class="abs fcol" style="left:784px;top:3486px"><h5>RECHTLICHES</h5><ul><li>AGB</li><li>Datenschutz</li><li>Cookies</li><li>Impressum</li></ul></div>
    <div class="abs bottom-bar">
      <span class="abs" style="left:47px;top:22px">© 2022 • Selvadon • Datenwerk GmbH</span>
      <span class="abs" style="left:707px;top:22px">UNSER PARTNER</span>
      <span class="abs" style="left:808px;top:14px;width:26px;height:26px;border-radius:50%;background:var(--green)"></span>
      <span class="abs" style="left:840px;top:21px">klare abläufe</span>
    </div>
  </footer>
</div>
</body>
</html>
```